Building Defect timeline illustration

We need an memorable illustration using iconography to plot the time frame for a building defects process. These are typically shown in single line format and not catchy. Designed to stand out. Powerpoint of the timeline attached. Colour blue to be dominant please.Can use building/construction imagery/icons.

Target Market(s)

Builders/Developers/General public

Industry/Entity Type

Property

Font styles to use
Sans Serif

Colors
0355a3
3176b5
ffffff

Requirements
Must have
• Visual appeal, ability to stick to the factual timeline.
Nice to have
• You could incorporate building/construction into the graphics- suggestion only.

```html
<!DOCTYPE html>
<html lang="en">
<head>
<meta charset="utf-8">
<title>Building Defect Bond Timeline</title>
<link href="https://fonts.googleapis.com/css2?family=Arimo:wght@400;700&display=swap" rel="stylesheet">
<style>
  :root {
    --blue: #1c72b8;
    --blue-light: #3176b5;
    --band-dark: #6d6e71;
    --band-light: #bcbdc0;
    --bubble: #bcbdc0;
    --frame: #4d4d4d;
    --ink: #000000;
    --white: #ffffff;
  }
  html, body {
    margin: 0;
    padding: 0;
    width: 1200px;
    height: 1000px;
    overflow: hidden;
    background: var(--white);
  }
  .timeline {
    display: block;
    width: 1200px;
    height: 1000px;
    font-family: "Arimo", Arial, sans-serif;
  }
  .frame { fill: var(--white); stroke: var(--frame); stroke-width: 1; }
  .band-light { fill: var(--band-light); }
  .band-dark { fill: var(--band-dark); }
  .chevron { fill: var(--white); }
  .bubble { fill: var(--bubble); }
  .bubble-text { font-size: 9px; fill: var(--ink); text-anchor: middle; }
  .step-label { font-size: 12.5px; font-weight: 700; fill: var(--ink); text-anchor: middle; }
  .badge-ring { fill: var(--white); }
  .badge { fill: var(--blue); }
  .icon-white { fill: var(--white); }
  .icon-line { stroke: var(--blue); stroke-width: 1.4; }
  .icon-stroke { fill: none; stroke: var(--white); stroke-width: 4; }
</style>
</head>
<body>
<svg class="timeline" viewBox="0 0 1200 1000" xmlns="http://www.w3.org/2000/svg">
  <rect class="frame" x="161.5" y="194.5" width="842" height="595"/>

  <!-- Bands -->
  <rect class="band-light" x="162" y="486" width="841" height="131"/>
  <rect class="band-dark" x="162" y="467" width="841" height="19"/>

  <!-- Chevrons -->
  <polygon class="chevron" points="286,496 301,540 286,584"/>
  <polygon class="chevron" points="433,496 448,540 433,584"/>
  <polygon class="chevron" points="580,496 595,540 580,584"/>
  <polygon class="chevron" points="727,496 742,540 727,584"/>
  <polygon class="chevron" points="872,496 887,540 872,584"/>

  <!-- Step 1 -->
  <g class="step">
    <rect class="bubble" x="176" y="295" width="90" height="112" rx="10"/>
    <polygon class="bubble" points="213,405 229,405 222,433"/>
    <text class="bubble-text" x="221" y="321">Any time before</text>
    <text class="bubble-text" x="221" y="332">OC issued</text>
    <circle class="badge-ring" cx="220" cy="483" r="47"/>
    <circle class="badge" cx="220" cy="483" r="42"/>
    <text x="220" y="500" font-size="48" font-weight="700" fill="#fff" text-anchor="middle">$</text>
    <text class="step-label" x="220" y="540">Lodge 2% Bond</text>
  </g>

  <!-- Step 2 -->
  <g class="step">
    <rect class="bubble" x="321" y="295" width="90" height="112" rx="10"/>
    <polygon class="bubble" points="358,405 374,405 367,433"/>
    <text class="bubble-text" x="366" y="321">Within 12 months</text>
    <text class="bubble-text" x="366" y="332">of completion of</text>
    <text class="bubble-text" x="366" y="343">building work*</text>
    <circle class="badge-ring" cx="365" cy="483" r="47"/>
    <circle class="badge" cx="365" cy="483" r="42" role="img" aria-label="Building inspector with hard hat and clipboard"/>
    <text class="step-label" x="366" y="540">Developer to</text>
    <text class="step-label" x="366" y="555">appoint building</text>
    <text class="step-label" x="366" y="570">inspector</text>
  </g>

  <!-- Step 3 -->
  <g class="step">
    <rect class="bubble" x="467" y="295" width="90" height="112" rx="10"/>
    <polygon class="bubble" points="504,405 520,405 513,433"/>
    <text class="bubble-text" x="512" y="321">Within 15 – 18</text>
    <text class="bubble-text" x="512" y="332">months of</text>
    <text class="bubble-text" x="512" y="343">completion of</text>
    <text class="bubble-text" x="512" y="354">building work</text>
    <circle class="badge-ring" cx="511" cy="483" r="47"/>
    <circle class="badge" cx="511" cy="483" r="42"/>
    <path class="icon-white" d="M495,458 h24 l8,8 v42 h-32 z"/>
    <g class="icon-line">
      <line x1="500" y1="478" x2="522" y2="478"/><line x1="500" y1="482" x2="522" y2="482"/>
      <line x1="500" y1="486" x2="522" y2="486"/><line x1="500" y1="490" x2="522" y2="490"/>
      <line x1="500" y1="494" x2="522" y2="494"/><line x1="500" y1="498" x2="522" y2="498"/>
      <line x1="500" y1="502" x2="522" y2="502"/>
    </g>
    <text class="step-label" x="512" y="540">Interim report to</text>
    <text class="step-label" x="512" y="555">be provided</text>
  </g>

  <!-- Step 4 -->
  <g class="step">
    <rect class="bubble" x="613" y="295" width="90" height="112" rx="10"/>
    <polygon class="bubble" points="650,405 666,405 659,433"/>
    <text class="bubble-text" x="658" y="321">Within 18 months</text>
    <text class="bubble-text" x="658" y="332">of completion of</text>
    <text class="bubble-text" x="658" y="343">building work</text>
    <circle class="badge-ring" cx="657" cy="483" r="47"/>
    <circle class="badge" cx="657" cy="483" r="42"/>
    <circle class="icon-stroke" cx="657" cy="483" r="29"/>
    <rect class="icon-white" x="641" y="481" width="7" height="17" rx="1"/>
    <path class="icon-white" d="M650,481 l8,-12 q2,-6 6,-4 q3,2 1,9 l-2,5 h11 q5,1 4,5 q-1,2 -2,3 q3,2 0,5 q2,3 -2,5 q1,4 -4,4 h-20 z"/>
    <text class="step-label" x="658" y="540">Developer to</text>
    <text class="step-label" x="658" y="555">arrange building</text>
    <text class="step-label" x="658" y="570">inspector to carry</text>
    <text class="step-label" x="658" y="585">out final inspection</text>
  </g>

  <!-- Step 5 -->
  <g class="step">
    <rect class="bubble" x="758" y="295" width="90" height="112" rx="10"/>
    <polygon class="bubble" points="795,405 811,405 804,433"/>
    <text class="bubble-text" x="803" y="321">21 to 24 months</text>
    <text class="bubble-text" x="803" y="332">after completion</text>
    <text class="bubble-text" x="803" y="343">of building work</text>
    <circle class="badge-ring" cx="803" cy="483" r="47"/>
    <circle class="badge" cx="803" cy="483" r="42"/>
    <rect class="icon-white" x="782" y="462" width="28" height="44" stroke="#1c72b8" stroke-width="1.5"/>
    <path class="icon-white" d="M792,455 h22 l8,8 v42 h-30 z" stroke="#1c72b8" stroke-width="1.5"/>
    <g class="icon-line">
      <line x1="797" y1="472" x2="818" y2="472"/><line x1="797" y1="476" x2="818" y2="476"/>
      <line x1="797" y1="480" x2="818" y2="480"/><line x1="797" y1="484" x2="818" y2="484"/>
      <line x1="797" y1="488" x2="818" y2="488"/><line x1="797" y1="492" x2="818" y2="492"/>
      <line x1="797" y1="496" x2="818" y2="496"/>
    </g>
    <text class="step-label" x="804" y="540">Final report to be</text>
    <text class="step-label" x="804" y="555">provided</text>
  </g>

  <!-- Step 6 -->
  <g class="step">
    <rect class="bubble" x="904" y="295" width="90" height="112" rx="10"/>
    <polygon class="bubble" points="941,405 957,405 950,433"/>
    <text class="bubble-text" x="949" y="321">2 years after</text>
    <text class="bubble-text" x="949" y="332">completion of</text>
    <text class="bubble-text" x="949" y="343">work within 60</text>
    <text class="bubble-text" x="949" y="354">days of date of</text>
    <text class="bubble-text" x="949" y="365">final inspection</text>
    <text class="bubble-text" x="949" y="376">report (whichever</text>
    <text class="bubble-text" x="949" y="387">is the later)</text>
    <circle class="badge-ring" cx="949" cy="483" r="47"/>
    <circle class="badge" cx="949" cy="483" r="42"/>
    <rect class="icon-white" x="927" y="462" width="44" height="40" rx="3"/>
    <rect x="930" y="472" width="38" height="27" fill="#1c72b8"/>
    <rect class="icon-white" x="933" y="456" width="3" height="10" rx="1.5"/>
    <rect class="icon-white" x="943" y="456" width="3" height="10" rx="1.5"/>
    <rect class="icon-white" x="953" y="456" width="3" height="10" rx="1.5"/>
    <rect class="icon-white" x="963" y="456" width="3" height="10" rx="1.5"/>
    <text x="949" y="495" font-size="18" font-weight="700" fill="#fff" text-anchor="middle">31</text>
    <text class="step-label" x="950" y="540">Last date for</text>
    <text class="step-label" x="950" y="555">claiming on bond</text>
  </g>
</svg>
</body>
</html>
```